New Fitness Company looking for creative website design

I am building a new fitness matching service. To match customers looking for fitness services to professionals that meet their requirements

My business will have 5 different divisions and I would like to have tabs for each division

1. Matching client to trainer - I need to have video upload capability on the site
2. Corporate personal training services

-The site needs a shopping cart as well as payment capability.
- I am looking for the site to be bright and inviting as well as have clients and trainers going through some type of workout on the main page.
- I also need the capability to capture email addresses
- We are going to have a section that ask the customer questions to match up the trainer so that needs to be a part of the site
-Ability to have trainers rated in a 1 star to 5 stars as well as reviews
- Site should be inviting, bright and vibrant colors that catch the eye and is easy to use
- Similar sites for inspiration are www.zorvanride.example where you give a description of how the service works, short video and various services.

Target Market(s)

mid income to high income, mix of female and male customers

Industry/Entity Type

Fitness

Coding

Coded - Design and coding required

Number of Pages Required

5+ page

Font styles to use
Serif
Sans Serif

Requirements
Must have
• Must have the logos that I provided in the website
Should not have
• Not looking for bodybuilders on website. This is for everyday people that are interested in staying in shape and working out. So active fit people will resonate with my prospects

```html
<!DOCTYPE html>
<html lang="en">
<head>
<meta charset="utf-8">
<title>Kestrel Fitness</title>
<link rel="stylesheet" href="https://fonts.googleapis.com/css2?family=Roboto:wght@400;500;700;900&family=Open+Sans:wght@400;600&display=swap">
<style>
:root{
  --green:#3db54a;
  --orange:#f7941d;
  --ink:#2b2b2b;
  --text:#6b6b6b;
  --muted:#9a9a9a;
  --light:#f3f3f3;
  --line:#e2e2e2;
  --dark:#1d1d1d;
  --dark-card:#2c2c2c;
  --footer:#121212;
  --white:#ffffff;
}
*{margin:0;padding:0;box-sizing:border-box}
html,body{width:1200px;height:3896px;overflow:hidden}
body{font-family:"Open Sans",Arial,sans-serif;color:var(--text);background:var(--white);position:relative}
.abs{position:absolute}
h1,h2,h3,.heading{font-family:"Roboto",Arial,sans-serif}

/* hero */
.hero{left:0;top:0;width:1200px;height:771px;background:radial-gradient(ellipse at 62% 35%,#5a5550 0%,#3a3734 45%,#1f1e1d 100%)}
.nav-top{right:70px;top:34px;display:flex;align-items:center;gap:18px;font:500 16px "Roboto",sans-serif;color:var(--white);letter-spacing:.5px}
.nav-top .sep{width:1px;height:18px;background:#888}
.burger{width:22px;height:14px;display:flex;flex-direction:column;justify-content:space-between}
.burger i{display:block;height:2px;background:#bbb}
.brand{left:0;width:1200px;top:132px;text-align:center}
.brand .dot{width:44px;height:44px;border-radius:50%;background:var(--green);margin:0 auto 12px}
.brand .name{font:900 34px "Roboto",sans-serif;color:var(--green);letter-spacing:2px;line-height:1}
.brand .name span{display:block;font-size:17px;letter-spacing:9px;margin-top:4px}
.hero-title{left:0;width:1200px;top:302px;text-align:center;font:700 58px "Roboto",sans-serif;color:var(--white);line-height:1}
.hero-sub{left:0;width:1200px;top:381px;text-align:center;font:700 41px "Roboto",sans-serif;color:var(--green)}
.hero-text{left:0;width:1200px;top:470px;text-align:center;font-size:16px;line-height:22px;color:#b9b9b9}
.mouse{left:587px;top:680px;width:26px;height:52px;border:2px solid #cfcfcf;border-radius:13px}
.mouse i{position:absolute;left:10px;top:9px;width:2px;height:10px;background:#cfcfcf}
.scroll-label{left:0;width:1200px;top:744px;text-align:center;font-size:11px;letter-spacing:2px;color:#aaa}
.scroll-line{top:748px;height:1px;width:36px;background:#999}

/* welcome */
.welcome{left:0;top:771px;width:1200px;height:533px;background:var(--light)}
.welcome .photo{left:0;top:0;width:530px;height:533px;background:linear-gradient(135deg,#dfe6ea 0%,#b7c3ca 45%,#c98f8a 100%)}
.play{left:225px;top:227px;width:80px;height:80px;border:4px solid var(--white);border-radius:50%}
.play svg{position:absolute;left:26px;top:20px}
.welcome h2{left:566px;top:80px;font:700 44px/52px "Roboto",sans-serif;color:var(--ink)}
.welcome h2 .g{color:var(--green)}
.welcome h2 .o{color:var(--orange)}
.welcome .copy{left:566px;top:212px;width:535px;font-size:13px;line-height:21px}
.welcome .rule{left:566px;top:304px;width:535px;height:1px;background:var(--line)}
.welcome .thumb{left:566px;top:330px;width:109px;height:68px;background:linear-gradient(135deg,#8ab86a,#4f7c39)}
.welcome .thumb-copy{left:695px;top:340px;width:400px;font-size:13px;line-height:22px;color:#555}
.btn{border:2px solid #333;font:700 12px "Roboto",sans-serif;color:var(--ink);letter-spacing:.5px;display:flex;align-items:center;justify-content:center;background:transparent}

/* corporate */
.section-title{left:0;width:1200px;text-align:center;font:700 46px/52px "Roboto",sans-serif;color:var(--ink)}
.corp-copy{left:99px;top:1536px;width:545px;font-size:13px;line-height:21px;text-align:justify}
.corp-photo{left:670px;top:1543px;width:431px;height:257px;background:linear-gradient(120deg,#e5ebef 0%,#c9d4da 50%,#9fb3bf 100%)}

/* trainers */
.trainer{width:491px;height:200px;background:var(--light)}
.trainer .pic{left:26px;top:-8px;width:125px;height:145px;border:6px solid var(--white);box-shadow:0 2px 6px rgba(0,0,0,.12)}
.trainer .socials{left:38px;top:150px;display:flex;gap:8px}
.trainer .socials i{display:block;width:26px;height:26px;border-radius:50%;background:var(--white);border:1px solid #ddd}
.trainer .name{left:170px;top:32px;font:700 12px "Roboto",sans-serif;color:var(--green);letter-spacing:.5px}
.trainer .name-rule{left:170px;top:50px;width:140px;height:1px;background:var(--line)}
.trainer .role{left:170px;top:62px;padding:5px 28px 5px 10px;background:#e2e2e2;clip-path:polygon(0 0,100% 0,88% 100%,0 100%);font-size:10px;color:#888;letter-spacing:.3px}
.trainer .stars{right:20px;top:30px;display:flex;gap:2px}
.trainer .bio{left:170px;top:100px;width:300px;font-size:12px;line-height:18px;color:var(--muted)}

/* products */
.products{left:0;top:2498px;width:1200px;height:608px;background:var(--dark)}
.products .section-title{color:var(--white)}
.product{top:156px;width:231px;height:369px}
.product .img{left:0;top:0;width:231px;height:197px;background:var(--white)}
.product .img i{position:absolute;left:30px;top:25px;width:171px;height:147px;background:radial-gradient(ellipse at center,#5a5f63 0%,#9aa0a4 55%,#ffffff 80%)}
.product .info{left:0;top:197px;width:231px;height:172px;background:var(--dark-card)}
.product.active .info{background:var(--green)}
.product .title{left:26px;top:40px;font:700 15px "Roboto",sans-serif;color:var(--white)}
.product .price{left:26px;top:66px;font:500 16px "Roboto",sans-serif;color:var(--white)}
.product .actions{left:0;top:130px;width:231px;height:42px;border-top:1px solid rgba(255,255,255,.12);display:flex;align-items:center;gap:18px;padding-left:26px;font-size:11px;color:#bdbdbd}
.product.active .actions{color:var(--white);border-top-color:rgba(255,255,255,.3)}
.product .actions span{display:flex;align-items:center;gap:6px}

/* faq */
.faq{width:491px;background:var(--light);border:1px solid #ececec}
.faq .num{left:0;top:0;width:47px;height:100%;border-right:1px solid var(--line);background:#f9f9f9;font:500 12px "Roboto",sans-serif;color:#444;padding-top:15px;text-align:center}
.faq .q{left:66px;top:15px;font-size:12px;color:#555}
.faq.open .q{color:var(--green)}
.faq .sign{right:14px;top:12px;font:400 16px "Roboto",sans-serif;color:#999}
.faq .a{left:66px;top:44px;width:400px;font-size:11px;line-height:18px;color:var(--muted)}

/* footer */
.footer{left:0;top:3594px;width:1200px;height:302px;background:var(--footer)}
.footer-nav{left:0;width:1200px;top:50px;display:flex;justify-content:center;gap:50px;font-size:12px;color:#9a9a9a}
.footer-nav .current{color:var(--white)}
.footer-rule{left:99px;top:108px;width:1002px;height:1px;background:#2a2a2a}
.footer-label{font:500 14px "Roboto",sans-serif;color:#cfcfcf}
.social-sq{top:172px;width:34px;height:34px}
.newsletter-input{left:462px;top:172px;width:166px;height:34px;background:#2a2a2a;font-size:11px;color:#777;padding:10px 14px}
.newsletter-btn{left:628px;top:172px;width:104px;height:34px;background:var(--orange);font:500 13px "Roboto",sans-serif;color:var(--white);display:flex;align-items:center;justify-content:center}
.contact{right:99px;top:167px;text-align:right;font-size:11px;line-height:15px;color:#8a8a8a}
.copyright{left:0;width:1200px;top:262px;display:flex;justify-content:center;align-items:center;gap:8px;font-size:11px;color:#777}
.copyright i{width:14px;height:14px;border-radius:50%;background:var(--green)}
</style>
</head>
<body>

<!-- hero -->
<section class="abs hero" role="img" aria-label="Smiling man working out with dumbbells in a bright gym, darkened as a backdrop"></section>
<nav class="abs nav-top"><span>CONTACT</span><span class="sep"></span><span>MENU</span><span class="burger"><i></i><i></i><i></i></span></nav>
<div class="abs brand">
  <div class="dot"></div>
  <div class="name">KESTREL<span>FITNESS</span></div>
</div>
<h1 class="abs hero-title">WE ARE</h1>
<p class="abs hero-sub heading">DAY TO DAY PEOPLE FITNESS</p>
<p class="abs hero-text">Larkspur is a research and analysis consultants<br>that helps to make solid decisions and drive results.</p>
<div class="abs mouse"><i></i></div>
<div class="abs scroll-line" style="left:499px"></div>
<div class="abs scroll-line" style="left:665px"></div>
<div class="abs scroll-label">SCROLL</div>

<!-- welcome -->
<section class="abs welcome">
  <div class="abs photo" role="img" aria-label="Man and woman doing sit-ups together on exercise balls"></div>
  <div class="abs play"><svg width="30" height="36" viewBox="0 0 30 36"><path d="M2 2 L28 18 L2 34 Z" fill="#fff"/></svg></div>
  <h2 class="abs">WELCOME TO<br><span class="g">KESTREL</span> <span class="o">FITNESS</span></h2>
  <p class="abs copy">Vestibulum tempor interdum tincidunt. Nam feugiat, metus nec laoreet volutpat, mi diam consectetur nisl, a vestibulum enim ligula a enim. Phasellus nec convallis lorem. Vestibulum a vestibulum enim ligula a enim. Phasellus nec convallis lorem.</p>
  <div class="abs rule"></div>
  <div class="abs thumb" role="img" aria-label="Small photo of a trainer outdoors"></div>
  <p class="abs thumb-copy">See how lorem ipsum dolor sit amet, consectetur adipiscing elit.<br>Quisque sit amet sollicitudin augue.</p>
  <div class="abs btn" style="left:566px;top:457px;width:151px;height:39px">READ MORE</div>
</section>

<!-- corporate training -->
<h2 class="abs section-title" style="top:1384px">CORPORATE<br>PERSONAL TRAINING</h2>
<p class="abs corp-copy">Nullam ullamcorper, libero eu maximus pharetra, nibh massa fermentum odio, eget bibendum velit nibh sed mauris. Duis at consequat turpis, vel feugiat odio. Vivamus vestibulum interdum erat. Suspendisse vel lacus vel odio elementum maximus efficitur nec felis. Duis justo tellus, dapibus ac congue sed, viverra ut eros. Class aptent taciti sociosqu ad litora torquent per conubia nostra, per inceptos himenaeos. Vestibulum quis volutpat lacus, a fringilla dolor. Aliquam vitae vehicula nulla. Nam elementum nunc enim, vitae venenatis sem sollicitudin nec. Vestibulum quis aliquet justo. Donec porttitor hendrerit odio, eu tincidunt enim commodo nec. Praesent gravida ex at mi fringilla consequat. Fusce gravida diam posuere, orci id, placerat purus. Aliquam sodales mauris ut nisl rutrum commodo. Morbi rhoncus magna sit amet est dictum tincidunt. Vestibulum in erat arcu.</p>
<div class="abs corp-photo" role="img" aria-label="Smiling man and woman with towels and water bottles after a workout"></div>
<div class="abs btn" style="left:493px;top:1761px;width:151px;height:39px">READ MORE</div>

<!-- trainers -->
<h2 class="abs section-title" style="top:1906px">OUR TRAINNERS</h2>

<div class="abs trainer" style="left:99px;top:2005px">
  <div class="abs pic" role="img" aria-label="Portrait of a young male trainer" style="background:linear-gradient(160deg,#c9ccd0,#7d858c)"></div>
  <div class="abs socials"><i></i><i></i><i></i></div>
  <div class="abs name">NADIA ROWE</div><div class="abs name-rule"></div>
  <div class="abs role">PHYSIO THERAPIST</div>
  <div class="abs stars"><svg width="80" height="14" viewBox="0 0 80 14"><g fill="#f7941d"><path id="st" d="M7 0l2 4.5 5 .5-3.8 3.3 1.1 4.9L7 10.7 2.7 13.2 3.8 8.3 0 5l5-.5z"/><use href="#st" x="16"/><use href="#st" x="32"/><use href="#st" x="48"/><use href="#st" x="64"/></g></svg></div>
  <p class="abs bio">Lorem ipsum dolor sit amet, consectetur adipiscing elit, sed do eiusmod tempor incididunt ut labore et dolore magna aliqua.</p>
</div>

<div class="abs trainer" style="left:610px;top:2005px">
  <div class="abs pic" role="img" aria-label="Portrait of a female trainer" style="background:linear-gradient(160deg,#d8b27a,#6e4a30)"></div>
  <div class="abs socials"><i></i><i></i><i></i></div>
  <div class="abs name">NADIA ROWE</div><div class="abs name-rule"></div>
  <div class="abs role">PHYSIO THERAPIST</div>
  <div class="abs stars"><svg width="80" height="14" viewBox="0 0 80 14"><g fill="#f7941d"><use href="#st"/><use href="#st" x="16"/><use href="#st" x="32"/><use href="#st" x="48"/></g><use href="#st" x="64" fill="#d6d6d6"/></svg></div>
  <p class="abs bio">Lorem ipsum dolor sit amet, consectetur adipiscing elit, sed do eiusmod tempor incididunt ut labore et dolore magna aliqua.</p>
</div>

<div class="abs trainer" style="left:99px;top:2233px">
  <div class="abs pic" role="img" aria-label="Portrait of a trainer with long hair" style="background:linear-gradient(160deg,#b06a7a,#4a2a3a)"></div>
  <div class="abs socials"><i></i><i></i><i></i></div>
  <div class="abs name">NADIA ROWE</div><div class="abs name-rule"></div>
  <div class="abs role">PHYSIO THERAPIST</div>
  <div class="abs stars"><svg width="80" height="14" viewBox="0 0 80 14"><g fill="#f7941d"><use href="#st"/><use href="#st" x="16"/><use href="#st" x="32"/><use href="#st" x="48"/></g><use href="#st" x="64" fill="#e0a860"/></svg></div>
  <p class="abs bio">Lorem ipsum dolor sit amet, consectetur adipiscing elit, sed do eiusmod tempor incididunt ut labore et dolore magna aliqua.</p>
</div>

<div class="abs trainer" style="left:610px;top:2233px">
  <div class="abs pic" role="img" aria-label="Portrait of a male trainer in a suit" style="background:linear-gradient(160deg,#a5563a,#2e2a2a)"></div>
  <div class="abs socials"><i></i><i></i><i></i></div>
  <div class="abs name">NADIA ROWE</div><div class="abs name-rule"></div>
  <div class="abs role">PHYSIO THERAPIST</div>
  <div class="abs stars"><svg width="80" height="14" viewBox="0 0 80 14"><g fill="#f7941d"><use href="#st"/><use href="#st" x="16"/><use href="#st" x="32"/><use href="#st" x="48"/><use href="#st" x="64"/></g></svg></div>
  <p class="abs bio">Lorem ipsum dolor sit amet, consectetur adipiscing elit, sed do eiusmod tempor incididunt ut labore et dolore magna aliqua.</p>
</div>

<!-- products -->
<section class="abs products">
  <h2 class="abs section-title" style="top:50px">OUR PRODUCTS</h2>

  <div class="abs product" style="left:99px">
    <div class="abs img" role="img" aria-label="Home gym multi-station machine"><i></i></div>
    <div class="abs info">
      <div class="abs title">Your Product Title</div><div class="abs price">$55.00</div>
      <div class="abs actions"><span><svg width="12" height="11" viewBox="0 0 12 11"><path d="M0 1h2l2 6h6l1.5-4H3" fill="none" stroke="currentColor" stroke-width="1.2"/><circle cx="5" cy="9.5" r="1" fill="currentColor"/><circle cx="9" cy="9.5" r="1" fill="currentColor"/></svg>Add to cart</span><span><svg width="10" height="12" viewBox="0 0 10 12"><path d="M1 .5h5.5l2.5 2.5v8.5H1z" fill="none" stroke="currentColor"/></svg>View detail</span></div>
    </div>
  </div>

  <div class="abs product active" style="left:356px">
    <div class="abs img" role="img" aria-label="Elliptical cross trainer"><i></i></div>
    <div class="abs info">
      <div class="abs title">Your Product Title</div><div class="abs price">$55.00</div>
      <div class="abs actions"><span><svg width="12" height="11" viewBox="0 0 12 11"><path d="M0 1h2l2 6h6l1.5-4H3" fill="none" stroke="currentColor" stroke-width="1.2"/><circle cx="5" cy="9.5" r="1" fill="currentColor"/><circle cx="9" cy="9.5" r="1" fill="currentColor"/></svg>Add to cart</span><span><svg width="10" height="12" viewBox="0 0 10 12"><path d="M1 .5h5.5l2.5 2.5v8.5H1z" fill="none" stroke="currentColor"/></svg>View detail</span></div>
    </div>
  </div>

  <div class="abs product" style="left:613px">
    <div class="abs img" role="img" aria-label="Weight bench with barbell plates"><i></i></div>
    <div class="abs info">
      <div class="abs title">Your Product Title</div><div class="abs price">$55.00</div>
      <div class="abs actions"><span><svg width="12" height="11" viewBox="0 0 12 11"><path d="M0 1h2l2 6h6l1.5-4H3" fill="none" stroke="currentColor" stroke-width="1.2"/><circle cx="5" cy="9.5" r="1" fill="currentColor"/><circle cx="9" cy="9.5" r="1" fill="currentColor"/></svg>Add to cart</span><span><svg width="10" height="12" viewBox="0 0 10 12"><path d="M1 .5h5.5l2.5 2.5v8.5H1z" fill="none" stroke="currentColor"/></svg>View detail</span></div>
    </div>
  </div>

  <div class="abs product" style="left:870px">
    <div class="abs img" role="img" aria-label="Black dumbbell"><i></i></div>
    <div class="abs info">
      <div class="abs title">Your Product Title</div><div class="abs price">$55.00</div>
      <div class="abs actions"><span><svg width="12" height="11" viewBox="0 0 12 11"><path d="M0 1h2l2 6h6l1.5-4H3" fill="none" stroke="currentColor" stroke-width="1.2"/><circle cx="5" cy="9.5" r="1" fill="currentColor"/><circle cx="9" cy="9.5" r="1" fill="currentColor"/></svg>Add to cart</span><span><svg width="10" height="12" viewBox="0 0 10 12"><path d="M1 .5h5.5l2.5 2.5v8.5H1z" fill="none" stroke="currentColor"/></svg>View detail</span></div>
    </div>
  </div>
</section>

<!-- faq -->
<h2 class="abs section-title" style="top:3145px">FAQ'S</h2>

<div class="abs faq" style="left:99px;top:3241px;height:47px"><div class="abs num">1</div><div class="abs q">Cum sociis natoque penatibus et ultrices volutpat?</div><div class="abs sign">+</div></div>
<div class="abs faq open" style="left:99px;top:3296px;height:124px"><div class="abs num">2</div><div class="abs q">Cum sociis natoque penatibus et ultrices volutpat?</div><div class="abs sign">&minus;</div><p class="abs a">Donec vestibulum justo a diam ultrices pellentesque. Quisque mattis diam vel lacus tincidunt elementum. Sed vitae adipiscing turpis. Aenean ligula nibh, molestie id viverra a, dapibus at dolor. In iaculis viverra neque, ac eleifend ante.</p></div>
<div class="abs faq" style="left:99px;top:3433px;height:47px"><div class="abs num">3</div><div class="abs q">Cum sociis natoque penatibus et ultrices volutpat?</div><div class="abs sign">+</div></div>

<div class="abs faq" style="left:610px;top:3241px;height:47px"><div class="abs num">4</div><div class="abs q">Cum sociis natoque penatibus et ultrices volutpat?</div><div class="abs sign">+</div></div>
<div class="abs faq" style="left:610px;top:3296px;height:124px"><div class="abs num">5</div><div class="abs q">Cum sociis natoque penatibus et ultrices volutpat?</div><div class="abs sign">+</div><p class="abs a">Donec vestibulum justo a diam ultrices pellentesque. Quisque mattis diam vel lacus tincidunt elementum. Sed vitae adipiscing turpis. Aenean ligula nibh, molestie id viverra a, dapibus at dolor. In iaculis viverra neque, ac eleifend ante.</p></div>
<div class="abs faq" style="left:610px;top:3433px;height:47px"><div class="abs num">6</div><div class="abs q">Cum sociis natoque penatibus et ultrices volutpat?</div><div class="abs sign">+</div></div>

<!-- footer -->
<footer class="abs footer">
  <nav class="abs footer-nav"><span class="current">Home</span><span>About us</span><span>Trainers</span><span>Blog</span><span>Events</span><span>Gallery</span><span>Contact Us</span></nav>
  <div class="abs footer-rule"></div>
  <div class="abs footer-label" style="left:99px;top:142px">Follow Us</div>
  <div class="abs social-sq" style="left:99px;background:#3b5998"></div>
  <div class="abs social-sq" style="left:139px;background:#1da1f2"></div>
  <div class="abs social-sq" style="left:179px;background:#dd4b39"></div>
  <div class="abs footer-label" style="left:0;width:1200px;text-align:center;top:142px">News letter</div>
  <div class="abs newsletter-input">Enter your email</div>
  <div class="abs newsletter-btn">Subscribe</div>
  <div class="abs footer-label" style="right:99px;top:142px">Contact Us</div>
  <div class="abs contact">Address<br>New Street<br>ph: xxxxx-xxx-xxx</div>
  <div class="abs copyright"><i></i>Kestrel &copy; 2015 Allright Reserved</div>
</footer>

</body>
</html>
```